Business Card Design

Our Pharmacy Opens late - the last to close in Brisbane
over 30 years since opened.
Open from 7am - 11pm every day.
Next to Corvale 7 Day Medical Centre
Parking in front of shop
Sit with a pharmacist for every script - the best advice every time.
Private consulting room.
We have the medication that you need.
Wide range Home Health Care products.

Looking for a card that my (young) staff feel happy to hand out to people they they meet.
Updates

Hello Many thanks for your submissions I just need to clarify the costings for this project as per my updated brief Please confirm then we can proceed Many thanks Gordon

Reason: due to the adjusted brief and query I have extended the deadline Many thanks for those that have submitted, I will choose the designer as soon as I understand the costings of the project, as per the message despatched today Regards gordon

Target Market(s)

men and women 30-70

Industry/Entity Type

Business

Contact Information for Business Card

Pelltons Pharmacy - Corvale
317 Baxwood Rd
Corvale 4279
Last to Close
Open 7am - 11pm

Font styles to use
Sans Serif

Requirements
Must have
• each batch of 250 will have the following staff names

Corinne Maltby, Senior Pharmacist
Talia Pronk, Pharmacist
Bo Wang, Pharmacist
Ilsabet Crowther, Pharmacist
Nadia Voss, Retail Manager
Lucy Trembath, Marketing Manager
Gordon Pelltons, Pharmacist Proprietor
Should not have
• Please advise if the cost of this job covers the 7 individualised business cards.

Each staff member needs their own card.

please advise

```html
<!DOCTYPE html>
<html lang="en">
<head>
<meta charset="utf-8">
<title>Pelltons Pharmacy – Business Card</title>
<link href="https://fonts.googleapis.com/css2?family=Arimo:ital,wght@0,400;0,700;1,400&display=swap" rel="stylesheet">
<style>
  :root {
    --backdrop: #e4e5e8;
    --card-white: #f6f6f6;
    --card-grey: #e9e9e9;
    --navy: #1f2d5c;
    --yellow: #e8ea3e;
    --yellow-deep: #dcdf2f;
    --ink: #111111;
    --white: #ffffff;
    --ghost: rgba(120, 125, 40, 0.28);
  }
  * { box-sizing: border-box; margin: 0; padding: 0; }
  html, body {
    width: 1200px;
    height: 523px;
    overflow: hidden;
    background: var(--backdrop);
    font-family: "Arimo", Arial, sans-serif;
  }
  .canvas {
    position: relative;
    width: 1200px;
    height: 523px;
    display: flex;
    align-items: center;
    justify-content: center;
  }
  .business-card {
    position: relative;
    width: 780px;
    height: 470px;
    background: var(--card-white);
    box-shadow: 0 6px 22px rgba(0, 0, 0, 0.18);
    overflow: hidden;
  }
  .card-top {
    position: absolute;
    inset: 0 0 auto 0;
    height: 222px;
    background: linear-gradient(135deg, var(--card-white) 0%, var(--card-grey) 100%);
  }
  .brand {
    position: absolute;
    left: 40px;
    top: 96px;
    display: flex;
    align-items: center;
    gap: 14px;
  }
  .brand-dot {
    width: 34px;
    height: 34px;
    border-radius: 50%;
    background: var(--navy);
  }
  .brand-name {
    font-size: 34px;
    font-weight: 700;
    color: var(--navy);
  }
  .staff {
    position: absolute;
    right: 34px;
    top: 40px;
    text-align: right;
  }
  .staff-name {
    font-size: 33px;
    font-weight: 700;
    color: var(--navy);
    letter-spacing: 0.5px;
  }
  .staff-role {
    font-size: 17px;
    font-style: italic;
    color: var(--ink);
    margin-top: 2px;
  }
  .address-band {
    position: absolute;
    left: 0;
    right: 0;
    top: 222px;
    height: 38px;
    background: var(--navy);
    color: var(--white);
    font-size: 21px;
    font-weight: 700;
    display: flex;
    align-items: center;
    justify-content: center;
  }
  .card-bottom {
    position: absolute;
    left: 0;
    right: 0;
    top: 260px;
    bottom: 0;
    background: linear-gradient(180deg, var(--yellow) 0%, var(--yellow-deep) 100%);
  }
  .contact {
    position: absolute;
    left: 46px;
    top: 42px;
    list-style: none;
    font-size: 21px;
    font-weight: 700;
    color: var(--ink);
    line-height: 1.35;
  }
  .brand-ghost {
    position: absolute;
    right: 30px;
    top: 40px;
    display: flex;
    align-items: center;
    gap: 16px;
  }
  .brand-ghost-dot {
    width: 60px;
    height: 60px;
    border-radius: 50%;
    background: var(--ghost);
  }
  .brand-ghost-name {
    font-size: 46px;
    font-weight: 700;
    color: var(--ghost);
  }
</style>
</head>
<body>
  <main class="canvas">
    <article class="business-card">
      <header class="card-top">
        <div class="brand">
          <span class="brand-dot"></span>
          <span class="brand-name">Pelltons Pharmacy</span>
        </div>
        <div class="staff">
          <h1 class="staff-name">CORINNE MALTBY</h1>
          <p class="staff-role">Senior Pharmacist</p>
        </div>
      </header>
      <div class="address-band">Corvale 317 Baxwood Rd Corvale 4279</div>
      <section class="card-bottom">
        <ul class="contact">
          <li>OPEN: 7am - 11pm</li>
          <li>Phone: 123-4567</li>
          <li>Email:</li>
        </ul>
        <div class="brand-ghost" aria-hidden="true">
          <span class="brand-ghost-dot"></span>
          <span class="brand-ghost-name">Pelltons Pharmacy</span>
        </div>
      </section>
    </article>
  </main>
</body>
</html>
```